Construction site banner with out Company information

I need a banner 4' tall and 6' wide, I want the banner to look very similar to the photo I uploaded from LumaDraw, make the person as life like as possible, I like the eyes to pop and be blue, and the hard hat orange, with the rest black and white, I have included our logo to use on the banner as well. Include the following:
Company Name: Brelvo Staffing
Temp Employees
General and Skilled Trades
Workers Comp and Payroll Coverage
www.tmkriv.com

Target Market(s)

Construction Companies

Requirements
Nice to have
• Realistic Person, bright blue eyes, orange hard hat
Should not have
• cartoon looking person

```html
<!DOCTYPE html>
<html lang="en">
<head>
<meta charset="utf-8">
<title>Brelvo Staffing – Construction Site Banner</title>
<link href="https://fonts.googleapis.com/css2?family=Poppins:wght@400;600;700&display=swap" rel="stylesheet">
<style>
  :root {
    --page-bg: #e9e9e9;
    --sign-black: #050505;
    --brand-orange: #f15a29;
    --band-orange-start: #f06a2c;
    --band-orange-end: #f7ab45;
    --text-white: #ffffff;
    --text-dark: #1e1e1e;
    --scene-dark: #1a1a1a;
    --scene-mid: #3a3a3a;
  }
  * { margin: 0; padding: 0; box-sizing: border-box; }
  html, body {
    width: 1200px; height: 1061px; overflow: hidden;
    background: var(--page-bg);
    font-family: "Poppins", sans-serif;
  }
  .banner {
    position: absolute; left: 40px; top: 157px;
    width: 1120px; height: 747px;
    background: var(--sign-black);
    overflow: hidden;
  }
  .site-scene {
    position: absolute; left: 0; top: 0; width: 760px; height: 700px;
    background: radial-gradient(ellipse at 65% 55%, var(--scene-mid) 0%, var(--scene-dark) 45%, var(--sign-black) 85%);
  }
  .worker-portrait {
    position: absolute; left: 560px; top: 0; width: 560px; height: 700px;
    background:
      radial-gradient(ellipse at 70% 10%, #ff5a1a 0%, #d8400e 22%, transparent 38%),
      radial-gradient(ellipse at 68% 55%, #9a7560 0%, #5a4234 35%, #1c1512 70%, var(--sign-black) 95%);
  }
  .brand-name {
    position: absolute; left: 49px; top: 70px;
    font-size: 112px; font-weight: 700; line-height: 1;
    color: var(--brand-orange); letter-spacing: -2px;
  }
  .service-title {
    position: absolute; left: 47px; top: 298px;
    font-size: 66px; font-weight: 700; line-height: 1;
    color: var(--brand-orange); letter-spacing: 1px;
  }
  .service-subtitle {
    position: absolute; left: 50px; top: 385px;
    font-size: 36px; font-weight: 600; line-height: 1;
    color: var(--text-white); letter-spacing: 1px;
  }
  .offer-band { position: absolute; left: 0; top: 0; width: 1120px; height: 747px; }
  .offer-list {
    position: absolute; left: 47px; top: 540px;
    list-style: none;
    font-size: 39px; font-weight: 700; line-height: 47px;
  }
  .offer-list .light { color: var(--text-white); }
  .offer-list .dark { color: var(--text-dark); }
  .web-address {
    position: absolute; right: 58px; top: 660px;
    font-size: 50px; font-weight: 400; line-height: 1;
    color: var(--text-white);
  }
  .web-address .domain { color: var(--brand-orange); }
</style>
</head>
<body>
  <main class="banner">
    <div class="site-scene" role="img" aria-label="Black and white photo of construction workers talking in front of scaffolding"></div>
    <div class="worker-portrait" role="img" aria-label="Realistic portrait of a bearded construction worker with bright blue eyes and an orange hard hat"></div>

    <div class="brand-name">Brelvo</div>
    <h1 class="service-title">STAFFING</h1>
    <p class="service-subtitle">TEMP EMPLOYEES</p>

    <svg class="offer-band" viewBox="0 0 1120 747" aria-hidden="true">
      <defs>
        <linearGradient id="bandGradient" x1="0" y1="0" x2="1" y2="0">
          <stop offset="0" stop-color="var(--band-orange-start)"/>
          <stop offset="1" stop-color="var(--band-orange-end)"/>
        </linearGradient>
      </defs>
      <path d="M0 520 H300 C420 520 480 545 540 610 C600 680 650 730 780 747 H0 Z" fill="url(#bandGradient)"/>
      <path d="M0 520 H300 C420 520 480 545 540 610 C600 680 650 730 780 747" fill="none" stroke="#ffffff" stroke-width="6"/>
    </svg>

    <ul class="offer-list">
      <li class="light">General and</li>
      <li class="light">Skilled Trades</li>
      <li class="dark">Workers Comp</li>
      <li class="dark">and Payroll Coverage</li>
    </ul>

    <p class="web-address"><span class="domain">tmkriv</span>.com</p>
  </main>
</body>
</html>
```